plumbing & gas fitting business card design

We need a business card design for a plumbing & gas fitting company. The company covers commercial, domestic and maintenance work. We would like a modern design communicating efficiency and sophistication. preferred colours would include (red grey & black) or (green grey & black). Please DO NOT include any water droplets.

Industry/Entity Type

Business

Contact Information for Business Card

Vortig Plumbing & Gas, Commercial Domestic & Maintenance, licence no. 617394K, ABN 47215830962, Phone 0417382956, Email vortigplumbingandgas@corvanet.com

```html
<!DOCTYPE html>
<html lang="en">
<head>
<meta charset="utf-8">
<title>Vortig Plumbing &amp; Gas — Business Card</title>
<link href="https://fonts.googleapis.com/css2?family=Source+Sans+3:wght@400;600&display=swap" rel="stylesheet">
<style>
  :root {
    --page-bg: #ffffff;
    --card-bg: #ffffff;
    --ink: #1e1e1e;
    --brand-green: #4a6244;
    --brand-green-light: #7c8a72;
    --ornament-gold: #e6cf94;
    --ornament-pale: #f6ecd0;
  }
  * { margin: 0; padding: 0; box-sizing: border-box; }
  html, body {
    width: 1200px;
    height: 1000px;
    overflow: hidden;
    background: var(--page-bg);
    font-family: "Source Sans 3", "Myriad Pro", sans-serif;
  }
  .card {
    position: absolute;
    left: 150px;
    top: 240px;
    width: 900px;
    height: 520px;
    background: var(--card-bg);
    box-shadow: 0 6px 18px rgba(0,0,0,0.35);
    overflow: hidden;
  }
  .card__ornament {
    position: absolute;
    left: 55px;
    top: 190px;
    width: 790px;
    height: 300px;
    background: radial-gradient(ellipse at 50% 55%, var(--ornament-gold) 0%, var(--ornament-pale) 45%, rgba(255,255,255,0) 72%);
    opacity: 0.8;
  }
  .card__brand {
    position: absolute;
    left: 0;
    right: 0;
    top: 95px;
    display: flex;
    justify-content: center;
    align-items: center;
    gap: 18px;
  }
  .card__brand-square {
    width: 44px;
    height: 44px;
    background: var(--brand-green);
  }
  .card__brand-name {
    font-size: 64px;
    font-weight: 600;
    color: var(--brand-green);
    line-height: 1;
  }
  .card__details {
    position: absolute;
    left: 0;
    right: 0;
    top: 248px;
    text-align: center;
    color: var(--ink);
  }
  .card__company {
    font-size: 38px;
    font-weight: 400;
    line-height: 1.15;
    margin-bottom: 6px;
  }
  .card__line {
    font-size: 23px;
    line-height: 1.3;
  }
</style>
</head>
<body>
  <main class="card">
    <div class="card__ornament" role="img" aria-label="Gold scrolling flourish ornament behind the contact details"></div>
    <div class="card__brand">
      <span class="card__brand-square"></span>
      <span class="card__brand-name">Vortig</span>
    </div>
    <div class="card__details">
      <h1 class="card__company">Vortig Plumbing &amp; Gas</h1>
      <p class="card__line">Commercial Domestic &amp; Maintenance,</p>
      <p class="card__line">licence no. 617394K,</p>
      <p class="card__line">ABN 47215830962,</p>
      <p class="card__line">Phone 0417382956,</p>
      <p class="card__line">Email - vortigplumbingandgas@corvanet.com</p>
    </div>
  </main>
</body>
</html>
```